Harvest Gathering event flyer

I would like a church event flyer designed. The event is called "HARVEST GATHERING 2018". I am looking for a professional, yet catchy design that uses our brand colors and logo creatively while communicating key information of the event effectively.

1. The logo is attached in two color formats. The designer has the choice to use them as he/she want.

2. The location of the event is: Lindqvist Community Center, 482 Tamsworth Street, Portland, ME 04102
3. Time and date of event. The designer can organize and format the date and time as he/she pleases.
December 28th, 29th @ 7:00PM
December 30th @ 10:00AM
4. The topic of the event is "Tongues of fire". The designer is free to use this phrase as he/she pleases to create a good composition.
5. Speaker: Prophet Marcus Obuya
6. Contact information: contact@cedarbrookfellowship.org - Telephone number: 207 555 0148

7. I would also like the following three words on the flyer. These words describe the focus of the event: FIRE, REVIVAL, PROPHETIC

```html
<!DOCTYPE html>
<html lang="en">
<head>
<meta charset="utf-8">
<title>Harvest Gathering 2018 Flyer</title>
<link rel="stylesheet" href="https://fonts.googleapis.com/css2?family=Oswald:wght@500;600&family=Dancing+Script:wght@700&display=swap">
<style>
  :root {
    --stage: #e9e9ea;
    --night: #05060a;
    --night-warm: #2a1a0c;
    --orange: #f3913a;
    --white: #ffffff;
    --navy: #1d3a5e;
    --navy-deep: #0f2742;
  }
  * { margin: 0; padding: 0; box-sizing: border-box; }
  html, body {
    width: 1200px; height: 581px; overflow: hidden;
    background: var(--stage);
  }
  .flyer {
    position: absolute; left: 394px; top: 0;
    width: 411px; height: 581px; overflow: hidden;
    background: var(--night);
    font-family: "Oswald", "Arial Narrow", sans-serif;
    color: var(--white);
  }
  .flyer__photo {
    position: absolute; inset: 0;
    background:
      radial-gradient(ellipse 60% 30% at 85% 12%, rgba(120,95,40,.55), transparent 70%),
      radial-gradient(ellipse 80% 28% at 50% 78%, rgba(190,140,70,.55), transparent 70%),
      radial-gradient(ellipse 40% 30% at 90% 55%, rgba(110,120,150,.45), transparent 70%),
      linear-gradient(180deg, var(--night) 0%, #0b0c14 40%, var(--night-warm) 75%, #3a2a1a 100%);
  }
  .flyer__footer-band {
    position: absolute; left: 0; right: 0; bottom: 0; height: 110px;
    background: linear-gradient(180deg, rgba(29,58,94,0) 0%, rgba(29,58,94,.85) 45%, var(--navy) 100%);
  }
  .headline { position: absolute; left: 26px; top: 14px; }
  .headline__line {
    display: flex; align-items: center; gap: 6px;
    font-weight: 600; text-transform: uppercase;
    line-height: 1; letter-spacing: .5px;
  }
  .headline__line--one { font-size: 50px; }
  .headline__line--two { font-size: 50px; color: var(--orange); margin-top: 2px; }
  .headline__line--year { font-size: 64px; margin-top: 4px; }
  .arrow { fill: var(--orange); flex: none; }
  .focus {
    position: absolute; left: 69px; top: 200px;
    font-size: 20px; font-weight: 500; color: var(--orange);
    letter-spacing: 1.8px; text-transform: uppercase; white-space: nowrap;
  }
  .schedule {
    position: absolute;
    font-family: "Dancing Script", cursive;
    font-weight: 700; font-size: 24px; color: var(--white);
    white-space: nowrap;
  }
  .schedule--evenings { left: 53px; top: 232px; }
  .schedule--morning { left: 83px; top: 270px; font-size: 23px; }
  .schedule__time { color: var(--orange); }
  .topic {
    position: absolute; left: 0; right: 0; top: 336px;
    text-align: center;
    font-family: "Dancing Script", cursive;
    font-weight: 700; font-size: 40px; color: var(--orange);
    line-height: 1;
  }
  .speaker {
    position: absolute; left: 0; right: 0; top: 388px;
    text-align: center;
    font-size: 17px; font-weight: 500; letter-spacing: 1.5px;
    text-transform: uppercase; color: var(--white);
  }
  .speaker__role { color: var(--orange); }
  .brand {
    position: absolute; left: 0; bottom: 0;
    width: 108px; height: 108px;
    background: var(--navy-deep);
    display: flex; flex-direction: column; align-items: center; justify-content: center; gap: 6px;
  }
  .brand__dot { width: 14px; height: 14px; border-radius: 50%; background: var(--orange); }
  .brand__name { font-size: 17px; font-weight: 500; color: var(--white); letter-spacing: .3px; }
  .contact {
    position: absolute; left: 140px; top: 490px;
    font-style: normal;
    font-size: 13.4px; font-weight: 600; line-height: 16.5px;
    color: var(--white); white-space: nowrap;
  }
</style>
</head>
<body>
  <article class="flyer">
    <div class="flyer__photo" role="img" aria-label="Night photograph of a festive main street with a white church steeple and buildings strung with warm holiday lights and coloured ornaments"></div>
    <div class="flyer__footer-band"></div>

    <h1 class="headline">
      <span class="headline__line headline__line--one">
        <svg class="arrow" width="40" height="44" viewBox="0 0 40 44"><polygon points="40,0 40,44 0,22"/></svg>
        Harvest
      </span>
      <span class="headline__line headline__line--two">Gathering</span>
      <span class="headline__line headline__line--year">
        2018
        <svg class="arrow" width="50" height="54" viewBox="0 0 50 54"><polygon points="0,0 0,54 50,27"/></svg>
      </span>
    </h1>

    <p class="focus">Fire, Revival, Prophetic</p>
    <p class="schedule schedule--evenings">December 28th, 29th @ <span class="schedule__time">7:00PM</span></p>
    <p class="schedule schedule--morning">December 30th @ <span class="schedule__time">10:00AM</span></p>

    <p class="topic">Tongues of Fire</p>
    <p class="speaker"><span class="speaker__role">Speaker:</span> Prophet Marcus Obuya</p>

    <div class="brand">
      <span class="brand__dot"></span>
      <span class="brand__name">Cedarbrook</span>
    </div>

    <address class="contact">
      contact@cedarbrookfellowship.org<br>
      207 555 0148<br>
      Lindqvist Community Center, 482 Tamsworth<br>
      Street, Portland, ME 04102
    </address>
  </article>
</body>
</html>
```